2022 Grenache Hillside Vineyard Sketch Wine Label

Size:4"X4"
Wine: 2022 Grenache
Vineyard Name: Low Mill Vineyard
AVA: Solano County
Alcohol by Volume:15%
Volume:750ml
Must Feature a hillside vineyard on the label somehow, I picture it being a sketch but it doesn't have to be. Not looking for anything flashy or colorful but maybe a pop of color somewhere. I am not yet sure that I want to include our name, but you can try to work in "KMT" somewhere on the label if it fits the design.
The Label must include all the information listed above. The Grenache was grown in a hillside vineyard, so I wanted the label to prominently feature a hillside vineyard. You can layout the label however you see best, but the vintage and varietal should be prominent, the ABV can be in small type face but must be legible following FQD guidelines. If you are able to make the vineyard name pop as well that would be good.
You don't have to use these, but our standard fonts we use are:
For Varietal: Bianca
Secondary (vintage, AVA, Vineyard):Helvetica
ABV/Volume: PT Serif
Thank you, look forward to the results

```html
<!DOCTYPE html>
<html lang="en">
<head>
<meta charset="utf-8">
<title>Grenache 2022 – Low Mill Vineyard</title>
<link rel="stylesheet" href="https://fonts.googleapis.com/css2?family=Playfair+Display:wght@800;900&family=Great+Vibes&family=Arimo&family=PT+Serif&display=swap">
<style>
  :root {
    --paper: #ffffff;
    --ink: #111111;
    --sky: #cfe3ee;
    --straw: #e6c98f;
    --vine: #8fa84f;
    --leaf-dark: #5f7d3a;
    --autumn: #d98a3a;
  }
  html, body {
    margin: 0;
    padding: 0;
    overflow: hidden;
    background: var(--paper);
  }
  .label {
    position: relative;
    width: 1200px;
    height: 1200px;
    background: var(--paper);
    color: var(--ink);
    overflow: hidden;
  }
  .label > * { position: absolute; margin: 0; }
  .varietal {
    top: 118px; left: 0; width: 100%;
    text-align: center;
    font-family: "Playfair Display", Georgia, serif;
    font-weight: 900;
    font-size: 78px;
    letter-spacing: 1px;
    line-height: 1;
  }
  .vintage {
    top: 226px; left: 0; width: 100%;
    text-align: center;
    font-family: "Playfair Display", Georgia, serif;
    font-weight: 800;
    font-size: 50px;
    line-height: 1;
  }
  .vineyard-name {
    top: 300px; left: 0; width: 100%;
    text-align: center;
    font-family: "Great Vibes", cursive;
    font-size: 118px;
    line-height: 1.1;
  }
  .hillside-scene {
    top: 535px; left: 215px;
    width: 770px; height: 350px;
  }
  .appellation {
    top: 955px; left: 0; width: 100%;
    text-align: center;
    font-family: "Arimo", Helvetica, Arial, sans-serif;
    font-size: 46px;
    letter-spacing: 3px;
    line-height: 1;
  }
  .alcohol, .volume {
    top: 1092px;
    font-family: "PT Serif", Georgia, serif;
    font-size: 40px;
    line-height: 1;
  }
  .alcohol { left: 136px; }
  .volume { right: 138px; top: 1100px; }
</style>
</head>
<body>
  <main class="label">
    <h1 class="varietal">GRENACHE</h1>
    <p class="vintage">2022</p>
    <p class="vineyard-name">Low Mill Vineyard</p>

    <svg class="hillside-scene" viewBox="0 0 770 350" role="img" aria-label="Watercolour sketch of a hillside vineyard with rows of vines, golden slopes and farmhouses on the ridge">
      <defs>
        <linearGradient id="scene-tone" x1="0" y1="0" x2="1" y2="1">
          <stop offset="0" stop-color="var(--sky)"/>
          <stop offset="0.3" stop-color="var(--straw)"/>
          <stop offset="0.6" stop-color="var(--vine)"/>
          <stop offset="0.78" stop-color="var(--autumn)" stop-opacity="0.8"/>
          <stop offset="1" stop-color="var(--leaf-dark)"/>
        </linearGradient>
      </defs>
      <path fill="url(#scene-tone)" opacity="0.85"
        d="M5 80 C60 40 140 20 230 40 C320 55 420 10 520 20 C600 28 680 30 765 45
           L765 215 C740 240 720 250 690 265 C620 290 560 320 480 335
           C400 348 320 330 260 300 C200 280 120 260 60 245 C30 235 10 200 5 170 Z"/>
    </svg>

    <p class="appellation">Solano County</p>
    <p class="alcohol">Alc. Vol. 15%</p>
    <p class="volume">Vol. 750 ml</p>
  </main>
</body>
</html>
```